The name of the company is Harbor Turns buying foreclosed homes and remodeling

A sleek classy card. It’s a home remodel and house flip company. Something mostly black with dark gray and red in color . Something with two f”s as a logo on front as shown in pictures. Kind of just let you guys run with it . I left a few pictures that should help
You guys get an idea of what I thought was good also left all the information for back of the card

Target Market(s)

Home remodel consumers

Industry/Entity Type

Construction Company

Contact Information for Business Card

All details are on photo

Font styles to use
Decorative

Colors

Designer to choose colors to be used in the design.

Requirements
Must have
• Name of company on front. Harbor Turns
Nice to have
• Up to you guys I trust you
Should not have
• Not sure

```html
<!DOCTYPE html>
<html lang="en">
<head>
<meta charset="utf-8">
<title>Harbor Turns — Business Card</title>
<link rel="stylesheet" href="https://fonts.googleapis.com/css2?family=Exo+2:wght@300;400&display=swap">
<style>
  :root {
    --page: #ffffff;
    --card: #4b4a48;
    --accent: #b04a38;
    --ink: #f1efeb;
  }
  * { margin: 0; padding: 0; box-sizing: border-box; }
  html, body {
    width: 993px; height: 1200px; overflow: hidden;
    background: var(--page);
    font-family: "Exo 2", Arial, sans-serif;
    color: var(--ink);
  }
  .sheet { position: relative; width: 993px; height: 1200px; }
  .card {
    position: absolute; left: 87px; width: 819px;
    background: var(--card); overflow: hidden;
  }
  .card--back  { top: 86px;  height: 469px; }
  .card--front { top: 645px; height: 469px; }
  .band { position: absolute; left: 0; right: 0; bottom: 0; background: var(--accent); }
  .card--back .band  { height: 105px; }
  .card--front .band { height: 22px; }
  .line { position: absolute; white-space: nowrap; line-height: 1; font-weight: 300; }
  .contact { left: 49px; font-size: 25px; }
  .contact--phone { top: 53px; }
  .contact--email { top: 85px; }
  .divider {
    position: absolute; left: 408px; top: 36px;
    width: 3px; height: 89px; background: var(--ink); border-radius: 2px;
  }
  .person { right: 39px; text-align: right; }
  .person__name  { top: 54px; font-size: 32px; font-weight: 400; }
  .person__title { top: 92px; font-size: 22px; }
  .brand {
    position: absolute; left: 0; right: 0; text-align: center;
  }
  .brand__name {
    display: block; font-size: 52px; font-weight: 300; line-height: 1;
    letter-spacing: 1px;
  }
  .brand__tagline {
    display: block; font-size: 21px; font-weight: 400; line-height: 1;
    letter-spacing: 1.5px; margin-top: 12px;
  }
  .card--back .brand,
  .card--front .brand { top: 223px; }
  .links {
    position: absolute; left: 0; right: 0; top: 23px;
    text-align: center; font-size: 25px; font-weight: 300; white-space: nowrap;
    line-height: 1;
  }
  .links__sep { display: inline-block; margin: 0 18px; font-size: 18px; vertical-align: 3px; }
</style>
</head>
<body>
<main class="sheet">
  <section class="card card--back" aria-label="Card back">
    <p class="line contact contact--phone">914-555-0173</p>
    <p class="line contact contact--email">DWhitcombeJr@example.com</p>
    <span class="divider"></span>
    <p class="line person person__name">Daniel Whitcombe Jr</p>
    <p class="line person person__title">General Contractor</p>
    <div class="brand" style="top:226px">
      <span class="brand__name">Harbor Turns</span>
      <span class="brand__tagline">Home Remodel</span>
    </div>
    <div class="band">
      <p class="links">www.harborturns.com<span class="links__sep">•</span>social.harborturns.com/turns</p>
    </div>
  </section>

  <section class="card card--front" aria-label="Card front">
    <div class="brand" style="top:226px">
      <span class="brand__name">Harbor Turns</span>
      <span class="brand__tagline">Home Remodel</span>
    </div>
    <div class="band"></div>
  </section>
</main>
</body>
</html>
```